Gourmet cookie company needs a label designed

We need a label designed for a new cookie company. We make mini cookies. The labels will be placed on either white tins or clear containers. We would like some bright and eye catching label although not child like. Our target customer is adults not kids.
Any color/colors acceptable. The initial label will be a square 4" label but the design should also be able to be formatted to fit on a round label as well in the future.

Text on label: Henrietta's Little Oven Company; Chocolate Chip; All Natural; New Wt. 8.0oz

```html
<!DOCTYPE html>
<html lang="en">
<head>
<meta charset="utf-8">
<title>Henrietta's Little Oven Company – Chocolate Chip Labels</title>
<link rel="stylesheet" href="https://fonts.googleapis.com/css2?family=Parisienne&family=Petit+Formal+Script&family=Carlito:wght@400;700&display=swap">
<style>
  :root {
    --page: #ffffff;
    --label-blue: #c5d5df;
    --ink: #000000;
    --paper: #ffffff;
    --guide: #4a5560;
    --caption: #333333;
    --cookie-light: #e4b27a;
    --cookie-dark: #b5763d;
  }
  html, body {
    margin: 0;
    padding: 0;
    width: 1200px;
    height: 900px;
    overflow: hidden;
    background: var(--page);
  }
  .label-sheet {
    display: block;
    width: 1200px;
    height: 900px;
  }
  .label-field { fill: var(--label-blue); }
  .brand-panel, .info-panel { fill: var(--ink); }
  .brand-name {
    font-family: "Parisienne", cursive;
    font-size: 42px;
    fill: var(--paper);
  }
  .brand-line {
    font-family: "Carlito", "Calibri", sans-serif;
    font-weight: 700;
    font-size: 15.5px;
    fill: var(--paper);
  }
  .flavour-name {
    font-family: "Petit Formal Script", cursive;
    font-weight: 400;
    font-size: 34px;
    letter-spacing: 2px;
    fill: var(--ink);
    stroke: var(--ink);
    stroke-width: 0.6px;
  }
  .natural-text {
    font-family: "Carlito", "Calibri", sans-serif;
    font-weight: 700;
    font-size: 15px;
    fill: var(--paper);
  }
  .net-weight {
    font-family: "Carlito", "Calibri", sans-serif;
    font-weight: 700;
    font-size: 13.5px;
    fill: var(--paper);
  }
  .cut-guide {
    fill: none;
    stroke: var(--guide);
    stroke-width: 0.8px;
    stroke-dasharray: 4 3;
  }
  .trim-frame {
    fill: none;
    stroke: var(--guide);
    stroke-width: 0.9px;
  }
  .size-caption {
    font-family: "Carlito", "Calibri", sans-serif;
    font-size: 12.5px;
    letter-spacing: 1px;
    fill: var(--caption);
  }
</style>
</head>
<body>
<svg class="label-sheet" viewBox="0 0 1200 900" xmlns="http://www.w3.org/2000/svg">
  <defs>
    <radialGradient id="cookie-tone" cx="40%" cy="45%" r="65%">
      <stop offset="0%" stop-color="var(--cookie-light)"/>
      <stop offset="100%" stop-color="var(--cookie-dark)"/>
    </radialGradient>
    <clipPath id="round-label-clip">
      <circle cx="956" cy="664" r="144"/>
    </clipPath>

    <g id="label-art">
      <rect class="brand-panel" x="289" y="151" width="222" height="144"/>
      <text class="brand-name" x="400" y="240" text-anchor="middle">Henrietta's</text>
      <text class="brand-line" x="400" y="273" text-anchor="middle">Little Oven Company</text>

      <text class="flavour-name" x="395" y="346" text-anchor="middle">Chocolate Chip</text>

      <rect class="cookie-photo" x="276" y="396" width="224" height="192" rx="70"
            fill="url(#cookie-tone)" role="img"
            aria-label="Photo of a stack of chocolate chip cookies with one cookie leaning against it"/>

      <rect class="info-panel" x="289" y="604" width="222" height="143"/>
      <text class="natural-text" x="400" y="663" text-anchor="middle">All Natural</text>
      <text class="net-weight" x="400" y="705" text-anchor="middle">NET WT.</text>
      <text class="net-weight" x="400" y="722" text-anchor="middle">8.0 oz</text>
    </g>
  </defs>

  <g class="square-label-large">
    <rect class="label-field" x="103" y="151" width="596" height="596"/>
    <rect class="cut-guide" x="112" y="160" width="578" height="578"/>
    <circle class="cut-guide" cx="401" cy="449" r="289"/>
    <use href="#label-art"/>
  </g>

  <g class="square-label-small">
    <rect class="label-field" x="812" y="80" width="288" height="288"/>
    <rect class="trim-frame" x="816" y="84" width="280" height="280"/>
    <rect class="trim-frame" x="820" y="88" width="272" height="272"/>
    <use href="#label-art" transform="translate(755.5 4.5) scale(0.5)"/>
    <text class="size-caption" x="970" y="395" text-anchor="middle">4”x4” Square Label</text>
  </g>

  <g class="round-label">
    <circle class="label-field" cx="956" cy="664" r="144"/>
    <circle class="trim-frame" cx="956" cy="664" r="140"/>
    <circle class="trim-frame" cx="956" cy="664" r="137"/>
    <g clip-path="url(#round-label-clip)">
      <use href="#label-art" transform="translate(755.5 442.5) scale(0.5)"/>
    </g>
    <text class="size-caption" x="969" y="830" text-anchor="middle">4”x4” Round Label</text>
  </g>
</svg>
</body>
</html>
```